" A LOJA VENTUZA IRA TRAZER UM SITE ECOOMERCE COM VENDAS DE PRODUTOS IMPORTADOS DA CHINA, OS PRODUTOS SAO VARIADOS EM CELULARES, RELOGIOS, PERIFÉRICOS, ROUPAS ETC.. "

```html
<!DOCTYPE html>
<html lang="pt-BR">
<head>
<meta charset="utf-8">
<title>Loja Ventuza – Cartão de visita</title>
<link rel="stylesheet" href="https://fonts.googleapis.com/css2?family=Roboto:wght@400;700&display=swap">
<style>
  :root {
    --bg: #e4e5e7;
    --blue-dark: #0a4f8f;
    --blue: #1a6fc0;
    --blue-light: #3a8fd8;
    --yellow: #f4c20d;
    --green: #5fb532;
    --white: #ffffff;
    --text-light: #dbe9f7;
    --brand-blue: #1e5fa8;
  }
  * { margin: 0; padding: 0; box-sizing: border-box; }
  html, body { width: 1200px; height: 1200px; overflow: hidden; }
  body {
    background: var(--bg);
    font-family: "Roboto", Arial, sans-serif;
    position: relative;
  }
  .card {
    position: absolute;
    left: 150px;
    width: 900px;
    height: 514px;
    box-shadow: 0 10px 30px rgba(0,0,0,.18);
  }
  .card-back {
    top: 70px;
    background: radial-gradient(ellipse at 80% 30%, var(--blue-light) 0%, var(--blue) 40%, var(--blue-dark) 100%);
    color: var(--white);
  }
  .card-front {
    top: 620px;
    background: var(--white);
  }
  .person {
    position: absolute;
    left: 70px;
    top: 150px;
    padding-left: 22px;
    border-left: 8px solid var(--yellow);
  }
  .person-name { font-size: 36px; font-weight: 700; }
  .person-role { font-size: 24px; color: var(--text-light); margin-top: 4px; }
  .contacts {
    position: absolute;
    left: 70px;
    top: 270px;
    list-style: none;
  }
  .contacts li {
    display: flex;
    align-items: center;
    gap: 26px;
    font-size: 22px;
    color: var(--text-light);
    height: 40px;
  }
  .contacts svg { width: 22px; height: 22px; flex: none; }
  .brand {
    position: absolute;
    display: flex;
    align-items: center;
    gap: 14px;
    font-weight: 700;
  }
  .brand-dot { border-radius: 50%; flex: none; }
  .card-back .brand { right: 60px; top: 260px; font-size: 38px; color: var(--white); }
  .card-back .brand-dot { width: 40px; height: 40px; background: var(--green); }
  .card-front .brand { left: 370px; top: 218px; font-size: 60px; color: var(--brand-blue); }
  .card-front .brand-dot { width: 62px; height: 62px; background: var(--green); }
</style>
</head>
<body>
  <section class="card card-back">
    <div class="person">
      <div class="person-name">Nome e Sobrenome</div>
      <div class="person-role">Cargo ou função</div>
    </div>
    <ul class="contacts">
      <li><svg viewBox="0 0 24 24"><path fill="#fff" d="M6.6 10.8a15 15 0 0 0 6.6 6.6l2.2-2.2a1 1 0 0 1 1-.25 11 11 0 0 0 3.6.6 1 1 0 0 1 1 1V20a1 1 0 0 1-1 1A17 17 0 0 1 3 4a1 1 0 0 1 1-1h3.5a1 1 0 0 1 1 1 11 11 0 0 0 .6 3.6 1 1 0 0 1-.25 1z"/></svg>+55 31 4000-1234</li>
      <li><svg viewBox="0 0 24 24"><rect x="2" y="5" width="20" height="14" fill="#fff"/><path d="M2 5l10 8 10-8" fill="none" stroke="#1a6fc0" stroke-width="2"/></svg>contato@lojaventuza.com.br</li>
      <li><svg viewBox="0 0 24 24"><circle cx="12" cy="12" r="9" fill="#fff"/></svg>lojaventuza</li>
      <li><svg viewBox="0 0 24 24"><circle cx="10" cy="10" r="6" fill="none" stroke="#fff" stroke-width="2.5"/><path d="M14.5 14.5L21 21" stroke="#fff" stroke-width="3"/></svg>www.lojaventuza.com.br</li>
      <li><svg viewBox="0 0 24 24"><path fill="#fff" d="M12 3l10 9h-3v9h-5v-6h-4v6H5v-9H2z"/></svg>Endereço completo</li>
    </ul>
    <div class="brand"><span class="brand-dot"></span>Loja Ventuza</div>
  </section>

  <section class="card card-front">
    <div class="brand"><span class="brand-dot"></span>Loja Ventuza</div>
  </section>
</body>
</html>
```